A4 Informational Flyer - Summer Pathology Course

We are looking to deliver a QRV27350 Certificate IV in Pathology Summer Course Specifically aimed at current University/TAFE students studying in a health related qualification e.g. Nursing students, Medical students, Pathology students etc.

The basis around it is that our potential students will complete this shortened summer course over the Christmas, new year break 2014/2015 which will enable them to gain further skills in the health related area and they will then be able to work in the pathology field whilst still studying - instead of working a side job at Brindleton's to support them.

We would like to use slogans on the flyer for engagement such as "Sick of flipping burgers?" "Are you looking to gain additional skills in a health related field" etc. anything you can come up with as the designer, is also welcomed.

Designer to include information regarding the course as follows:

Course Introduction:

This is a National Training Package and is designed to train people wishing to pursue a career in the Pathology Collection Industry.
The modules within QRV27350 Certificate IV in Pathology provide the participants with training and skills development in a range of areas including Customer Service, Pathology Collection and Techniques, Phlebotomy (blood collection), Infection Control, Occupational Health and Safety and knowledge of the disease processes associated with clients of all ages who may require Pathology Collection.

Government Funding is available for eligible students.

Fees:

Government Funded Student Fees:
Tuition: $425
If you also have a healthcare card, $85
Resources: $355

Fee For Service Student Fees:
Tuition: $2,365
Resources: $355

Method of Study:

The summer QRV27350 Certificate IV in Pathology program is run on campus at both our Harrowfield and Quenby training facilities. Students will attend classes two (2) days per week from 9.30am to 2.30pm. Some workbooks are required to be completed off-campus. Extensive practical experience is undertaken in the Vexmoor Learning Hub clinical laboratories.

Course Commencement & Duration:

Course will commence late November 2014 and includes one (1) fast track week and one (1) 4 day week. Classes will conclude by the late January 2015. (Includes 2 week break over Christmas/New Year). *Subject to student numbers

Application Process:

Complete an online enrollment form via our website www.vexmoorlearninghub.edu.au and our student administration will contact you within 24 hours to discuss your enrollment and the next steps to secure your place on the course.
Alternatively, contact one of our friendly staff members on 03 7215 6048 for further assistance and information.

Please include our attached logos, photos for engagement etc where appropriate.
Please include our website in bold: www.vexmoorlearninghub.edu.au and our phone number is bold 03 7215 6048

Please also include our "TOID No. 31785" under our logo.

We would like this overall flyer/brochure to be engaging, bold, simply, easy to read for potential students. Keeping with our company colors as much as possible is a must.

Formats must be in a normal format such as PDF for printing purposes and also a JPEG, ESP format so we can use to advertise as a picture on Pinwheelia etc.

Industry/Entity Type

Healthcare

Font styles to use
Serif

Colors
f37123
ffc214
faa54b

Requirements
Must have
• A4, 1 sided please.

Must include codes next to course title.

```html
<!DOCTYPE html>
<html lang="en">
<head>
<meta charset="utf-8">
<title>Vexmoor Learning Hub – Summer Pathology Course</title>
<link href="https://fonts.googleapis.com/css2?family=Oswald:wght@500;600;700&family=Lato:wght@400;700;900&display=swap" rel="stylesheet">
<style>
  :root{
    --orange:#f15a24;
    --orange-soft:#f37123;
    --yellow:#ffc814;
    --fee-red:#b3200f;
    --fee-orange:#d9540f;
    --charcoal:#3f3f41;
    --grey-text:#4b4b4d;
    --white:#ffffff;
    --page:#e6e6e6;
  }
  *{margin:0;padding:0;box-sizing:border-box}
  html,body{width:950px;height:1200px;overflow:hidden;background:var(--page)}
  .flyer{position:absolute;left:54px;top:10px;width:841px;height:1180px;background:var(--white);overflow:hidden;font-family:'Lato',sans-serif;box-shadow:0 2px 10px rgba(0,0,0,.15)}
  .backdrop{position:absolute;inset:0}

  .brand{position:absolute;left:70px;top:70px;width:200px;text-align:center}
  .brand-mark{width:70px;height:70px;border-radius:50%;background:var(--orange-soft);margin:0 auto 22px}
  .brand-name{font-family:'Lato',sans-serif;font-weight:700;color:var(--orange-soft);font-size:24px;line-height:1.1}
  .brand-toid{margin-top:8px;font-weight:700;color:var(--grey-text);font-size:15px;letter-spacing:.5px}

  .fees{position:absolute;left:47px;top:248px;width:256px;height:410px;background:var(--yellow);border-radius:0 0 22px 22px;text-align:center;padding-top:26px}
  .fees-title{font-family:'Oswald',sans-serif;font-weight:700;font-size:50px;line-height:1;color:var(--charcoal)}
  .fees-group{font-weight:700;font-size:16px;color:var(--fee-orange);line-height:1.3;margin-top:10px}
  .fees-line{font-family:'Oswald',sans-serif;font-weight:600;font-size:25px;color:var(--charcoal);line-height:1.25;margin-top:8px}
  .fees-line em{font-style:normal;color:var(--fee-red)}
  .fees-note{font-weight:700;font-size:15px;color:var(--charcoal);line-height:1.3;margin-top:6px}
  .fees-note em{font-style:normal;color:var(--fee-red);font-family:'Oswald',sans-serif;font-size:18px}
  .fees-line.large{font-size:32px;line-height:1.05;margin-top:0}

  .intro{position:absolute;left:320px;top:372px;width:500px;color:var(--white)}
  .intro-title{font-family:'Lato',sans-serif;font-weight:700;font-size:30px;display:flex;align-items:center;gap:8px}
  .intro-title::after{content:"";flex:1;height:9px;border-top:2px solid var(--white);border-bottom:2px solid var(--white);margin-top:8px;max-width:150px}
  .intro p{font-weight:700;font-size:14px;line-height:1.22;margin-top:10px}
  .funding{position:absolute;left:323px;top:582px;width:360px;height:60px;background:var(--white);border-radius:20px;border:3px solid #d8d8d8;padding:6px 20px;font-weight:700;font-size:19px;line-height:1.2;color:var(--grey-text)}

  .section-title{font-family:'Oswald',sans-serif;font-weight:600;color:var(--orange);text-align:right;line-height:1}
  .rule{position:relative;height:2px;background:var(--charcoal);margin-top:6px}
  .rule::before{content:"";position:absolute;left:-4px;top:-4px;width:10px;height:10px;border-radius:50%;background:var(--charcoal)}
  .method{position:absolute;left:340px;top:705px;width:478px}
  .method .section-title{font-size:40px}
  .method p,.timing p{font-weight:700;font-size:15px;line-height:1.25;color:var(--grey-text);text-align:right;margin-top:10px}
  .timing{position:absolute;left:340px;top:905px;width:478px}
  .timing .section-title{font-size:33px}
  .timing p{margin-left:30px;margin-top:8px}

  .contact{position:absolute;left:0;right:0;top:1122px;text-align:center;color:var(--white);font-weight:900;font-size:25px;display:flex;justify-content:center;align-items:center;gap:10px}
  .contact svg{flex:none}
</style>
</head>
<body>
<div class="flyer">
  <svg class="backdrop" width="841" height="1180" viewBox="0 0 841 1180">
    <defs>
      <linearGradient id="classroomTone" x1="0" y1="0" x2="1" y2="1">
        <stop offset="0" stop-color="#f2f2f0"/>
        <stop offset="0.55" stop-color="#e2dcd6"/>
        <stop offset="1" stop-color="#c9a28f"/>
      </linearGradient>
      <linearGradient id="studentTone" x1="0" y1="0" x2="0" y2="1">
        <stop offset="0" stop-color="#e8d9b8"/>
        <stop offset="0.6" stop-color="#e3c3ad"/>
        <stop offset="1" stop-color="#555358"/>
      </linearGradient>
    </defs>
    <g role="img" aria-label="Photo of a tutor in a white coat teaching beside an anatomy model">
      <polygon points="293,0 841,0 841,350 293,290" fill="url(#classroomTone)"/>
    </g>
    <g role="img" aria-label="Photo of a smiling young student">
      <rect x="0" y="690" width="322" height="370" fill="url(#studentTone)"/>
    </g>
    <polygon points="0,248 841,340 841,372 0,292" fill="var(--charcoal)"/>
    <polygon points="0,286 841,368 841,645 0,708" fill="var(--orange)"/>
    <polygon points="0,708 841,645 841,678 0,742" fill="var(--charcoal)"/>
    <polygon points="0,742 841,678 841,686 0,750" fill="#ededed"/>
    <polygon points="0,1022 841,1090 841,1112 0,1052" fill="var(--charcoal)"/>
    <polygon points="0,1052 841,1108 841,1180 0,1180" fill="var(--orange)"/>
  </svg>

  <div class="brand">
    <div class="brand-mark"></div>
    <div class="brand-name">Vexmoor Learning Hub</div>
    <div class="brand-toid">TOID No. 31785</div>
  </div>

  <div class="fees">
    <div class="fees-title">Fees</div>
    <div class="fees-group">Government Funded<br>Student Fees:</div>
    <div class="fees-line">Tuition: <em>$425</em></div>
    <div class="fees-note">If you also have a<br>healthcare card, <em>$85</em></div>
    <div class="fees-line">Resources: <em>$355</em></div>
    <div class="fees-group">Fee For Service Student Fees:</div>
    <div class="fees-line">Tuition: <em>$2,365</em></div>
    <div class="fees-line large">Resources</div>
    <div class="fees-line large"><em>$355</em></div>
  </div>

  <div class="intro">
    <h2 class="intro-title">Course Introduction:</h2>
    <p>This is a National Training Package and is designed to train people wishing to pursue a career in the Pathology Collection Industry.</p>
    <p>The modules within QRV27350 Certificate IV in Pathology provide the participants with training and skills development in a range of areas including Customer Service, Pathology Collection and Techniques, Phlebotomy (blood collection), Infection Control, Occupational Health and Safety and knowledge of the disease processes associated with clients of all ages who may require Pathology Collection.</p>
  </div>
  <div class="funding">Government Funding is available for eligible students.</div>

  <div class="method">
    <h2 class="section-title">Method of Study</h2>
    <div class="rule"></div>
    <p>The summer QRV27350 Certificate IV in Pathology program is run on campus at both our Harrowfield and Quenby training facilities. Students will attend classes two (2) days per week from 9.30am to 2.30pm. Some workbooks are required to be completed off-campus. Extensive practical experience is undertaken in the Vexmoor Learning Hub clinical laboratories.</p>
  </div>

  <div class="timing">
    <h2 class="section-title">Course Commencement &amp; Duration</h2>
    <div class="rule"></div>
    <p>Course will commence late November 2014 and includes one (1) fast track week and one (1) 4 day week. Classes will conclude by the late January 2015. (Includes 2 week break over Christmas/New Year). *Subject to student numbers</p>
  </div>

  <div class="contact">
    <svg width="24" height="24" viewBox="0 0 24 24" fill="none" stroke="#fff" stroke-width="1.8" aria-hidden="true">
      <circle cx="12" cy="12" r="10"/><ellipse cx="12" cy="12" rx="4.5" ry="10"/><line x1="2" y1="12" x2="22" y2="12"/><path d="M4 6.5h16M4 17.5h16"/>
    </svg>
    <span>www.vexmoorlearninghub.edu.au</span>
    <svg width="22" height="22" viewBox="0 0 22 22" aria-hidden="true">
      <rect width="22" height="22" rx="3" fill="#fff"/>
      <path d="M7 4.5l2.3 3-1.4 1.6c.9 1.9 2.3 3.3 4.1 4.2l1.6-1.4 3 2.3-1.2 2.4c-5.3-.6-9.4-4.7-10-10z" fill="var(--orange)"/>
    </svg>
    <span>03 7215 6048</span>
  </div>
</div>
</body>
</html>
```